Real Estate 2015 sold listings postcard

Real estate. I want one side to list 2015 sales. Mailing side with additional information. I am including a "concept" but it needs to be professionalized... Feel free to change color, fonts, layout, add watermark, whatever you think will work. Text on backside may be tweaked. I do want postcards addressed. How do i send mailing list or does Quorra Mail do that part?

NOTE: Postcard should be 8.5 x 5.5 inches.

postcard should be 8.5" x 5.5" size

Target Market(s)

Home owners who may want to sell

Industry/Entity Type

Real Estate Agent

Requirements
Must have
• The sold information and contact oinformation I have provided
Nice to have
• Watermark with my initials

```html
<!DOCTYPE html>
<html lang="en">
<head>
<meta charset="utf-8">
<title>2015 Sales Postcard</title>
<link href="https://fonts.googleapis.com/css2?family=Montserrat:wght@500;700;800&family=Roboto+Condensed:wght@400;700&family=Kaushan+Script&display=swap" rel="stylesheet">
<style>
:root{
  --blue:#0a5ea8;
  --blue-dark:#06498a;
  --row-alt:#d6ebf8;
  --band:#9fd0f2;
  --ink:#111;
  --red:#c8141c;
  --gold:#b08a2a;
  --bg:#ececec;
  --paper:#fff;
}
*{box-sizing:border-box;margin:0;padding:0}
html,body{width:1200px;height:1000px;overflow:hidden;background:var(--bg)}
body{position:relative;font-family:"Roboto Condensed",Arial,sans-serif;color:var(--ink)}
.card{position:absolute;background:var(--paper);box-shadow:0 1px 4px rgba(0,0,0,.25)}
.front{left:40px;top:28px;width:710px;height:460px}
.back{left:446px;top:512px;width:711px;height:460px;overflow:hidden}

/* front */
.brand-box{position:absolute;left:30px;top:12px;width:116px;height:53px;border:1px solid #bbb;border-radius:6px;background:#fff;display:flex;align-items:center;justify-content:center;gap:5px}
.brand-box .mark{width:10px;height:10px;background:var(--gold)}
.brand-name{font-family:"Montserrat",sans-serif;font-weight:700;font-size:11px;color:var(--ink);letter-spacing:.5px}
.title-band{position:absolute;left:150px;top:20px;width:547px;height:34px;background:var(--blue);color:#fff;font-family:"Montserrat",sans-serif;font-weight:800;font-size:20px;line-height:34px;padding-left:14px}
.sold-rule{position:absolute;left:14px;top:80px;width:683px;height:2px;background:#222}
.sold-label{position:absolute;left:313px;top:68px;padding:0 6px;background:#fff;border-left:2px solid #222;border-right:2px solid #222;font-family:"Montserrat",sans-serif;font-weight:800;font-size:22px;color:var(--blue);line-height:26px}
.sales-head{position:absolute;left:14px;top:96px;width:683px;height:22px;background:var(--blue);border-radius:6px 6px 0 0}
.sales-wrap{position:absolute;left:14px;top:96px;width:683px;height:276px;border:1px solid #8aa;border-radius:6px;overflow:hidden}
.sales{width:100%;border-collapse:collapse;table-layout:fixed;font-size:11px;font-weight:700}
.sales th{height:24px;color:#fff;font-size:13px;font-weight:700;text-align:left}
.sales td{height:15.5px;line-height:15.5px;white-space:nowrap}
.sales tbody tr:nth-child(odd){background:var(--row-alt)}
.sales .c{text-align:center}
.sales .r{text-align:right}
.sales th:first-child,.sales td:first-child{padding-left:12px}
.agent-photo{position:absolute;left:108px;top:376px;width:57px;height:74px;background:linear-gradient(#6a3a2a,#b0242a);border:1px solid #999}
.agent-line{position:absolute;left:176px;top:378px;display:flex;align-items:baseline;gap:6px;font-family:"Montserrat",sans-serif;font-size:12px}
.agent-sig{font-family:"Kaushan Script",cursive;color:var(--red);font-size:19px}
.contact-band{position:absolute;left:14px;top:405px;width:683px;height:29px;background:var(--band);display:flex;align-items:center;gap:26px;padding-left:162px;font-family:"Montserrat",sans-serif;font-size:13.5px;font-weight:500}
.contact-band span{display:flex;align-items:center;gap:4px}
.disclaimer{position:absolute;left:186px;top:438px;font-size:9px;font-weight:700}

/* back */
.side-panel{position:absolute;left:0;top:0;width:360px;height:460px;background:linear-gradient(90deg,#fff 75%,#e8e8e8)}
.lead{position:absolute;left:26px;top:16px;width:310px;font-size:17px;font-weight:700;color:var(--blue);line-height:21px}
.checks{position:absolute;left:26px;top:62px;display:flex;gap:26px;font-size:12px;font-style:italic}
.checks span{display:flex;align-items:center;gap:3px}
.reach{position:absolute;left:26px;top:85px;font-size:14.5px}
.reach b{color:var(--blue)}
.cta{position:absolute;left:30px;top:114px;width:301px;height:26px;border:2px solid #222;border-radius:8px;background:#bfe0f6;font-size:15px;font-weight:700;line-height:22px;text-align:center}
.cta em{font-style:normal;color:var(--blue)}
.body-copy{position:absolute;left:27px;top:156px;width:310px;font-size:9.6px;line-height:12.8px}
.body-copy p+p{margin-top:12px}
.back-band{position:absolute;left:28px;top:366px;width:332px;height:67px;background:var(--blue);border-radius:14px 0 0 0}
.back-photo{position:absolute;left:46px;top:324px;width:70px;height:109px;background:linear-gradient(#5a3326,#c0212a)}
.back-name{position:absolute;left:122px;top:390px;color:#fff;font-size:17px;font-weight:700}
.back-name small{font-weight:400;font-size:13px;margin-left:6px}
.back-contact{position:absolute;left:122px;top:413px;color:#fff;font-size:12.5px}
.stamp{position:absolute;left:602px;top:19px;width:90px;height:108px;border:1px solid #888}
.back-brand{position:absolute;left:430px;top:380px;width:210px;display:flex;align-items:center;justify-content:center;gap:8px}
.back-brand .mark{width:16px;height:16px;background:var(--gold)}
.back-brand .brand-name{font-size:18px}
.back-web{position:absolute;left:475px;top:420px;font-family:"Montserrat",sans-serif;font-size:12.5px;display:flex;align-items:center;gap:3px}
</style>
</head>
<body>

<section class="card front">
  <div class="brand-box"><span class="mark"></span><span class="brand-name">HARBOR CREST</span></div>
  <h1 class="title-band">2015 SALES IN YOUR NEIGHBORHOOD</h1>
  <div class="sold-rule"></div>
  <div class="sold-label">SOLD</div>
  <div class="sales-head"></div>
  <div class="sales-wrap">
    <table class="sales">
      <colgroup><col style="width:118px"><col style="width:30px"><col style="width:40px"><col style="width:72px"><col style="width:70px"><col style="width:100px"><col style="width:110px"><col style="width:80px"><col style="width:50px"><col></colgroup>
      <thead><tr><th>Address</th><th>BR</th><th>BA</th><th>SqFt</th><th class="r">Lot Size</th><th class="r">Lot Price</th><th class="c">Sale Price</th><th class="c">$/Sq. Ft</th><th class="c">DOM</th><th></th></tr></thead>
      <tbody>
        <tr><td>387 Alder PL*</td><td>3</td><td>3 ½</td><td class="r">2588</td><td class="r">9239</td><td class="r">3088000</td><td class="c">3,100,000</td><td class="c">1198</td><td class="c">9</td><td></td></tr>
        <tr><td>3657 Birch ST</td><td>4</td><td>3</td><td class="r">2228</td><td class="r">6147</td><td class="r">2998000</td><td class="c">3000000</td><td class="c">1346</td><td class="c">23</td><td></td></tr>
        <tr><td>261 Brookview DR</td><td>4</td><td>3</td><td class="r">2185</td><td class="r">7040</td><td class="r">2500000</td><td class="c">2925000</td><td class="c">1,339</td><td class="c">9</td><td></td></tr>
        <tr><td>437 Fenwick AVE*</td><td>4</td><td>2</td><td class="r">1611</td><td class="r">13,237</td><td class="r">2498000</td><td class="c">2610000</td><td class="c">1620</td><td class="c">8</td><td></td></tr>
        <tr><td>4123 Dalton AVE*</td><td>4</td><td>2</td><td class="r">2227</td><td class="r">8700</td><td class="r">2295000</td><td class="c">2595000</td><td class="c">1165</td><td class="c">8</td><td></td></tr>
        <tr><td>76 Ridgeway CIR*</td><td>3</td><td>2</td><td class="r">1364</td><td class="r">5917</td><td class="r">1788000</td><td class="c">2525000</td><td class="c">1851</td><td class="c">8</td><td></td></tr>
        <tr><td>3665 Rosalind CIR</td><td>4</td><td>2</td><td class="r">1646</td><td class="r">6404</td><td class="r">2500000</td><td class="c">2475000</td><td class="c">1504</td><td class="c">18</td><td></td></tr>
        <tr><td>410 Aspen PL*</td><td>3</td><td>2</td><td class="r">1674</td><td class="r">11200</td><td class="r">2498000</td><td class="c">2450000</td><td class="c">1464</td><td class="c">16</td><td></td></tr>
        <tr><td>291 Brookview DR*</td><td>4</td><td>2</td><td class="r">1690</td><td class="r">8178</td><td class="r">2199000</td><td class="c">240000</td><td class="c">1420</td><td class="c">7</td><td></td></tr>
        <tr><td>303 Brookview DR</td><td>3</td><td>2</td><td class="r">1674</td><td class="r">8538</td><td class="r">2200000</td><td class="c">2260000</td><td class="c">1350</td><td class="c">97</td><td></td></tr>
        <tr><td>93 Ridgeway CIR</td><td>3</td><td>2</td><td class="r">1243</td><td class="r">6080</td><td class="r">1488000</td><td class="c">2250000</td><td class="c">1810</td><td class="c">7</td><td></td></tr>
        <tr><td>3702 Carver CIR*</td><td>4</td><td>2</td><td class="r">13333</td><td class="r">6493</td><td class="r">1895000</td><td class="c">2227500</td><td class="c">1671</td><td class="c">6</td><td></td></tr>
        <tr><td>372 Parkview DR*</td><td>3</td><td>2</td><td class="r">1740</td><td class="r">6324</td><td class="r">2200000</td><td class="c">2180000</td><td class="c">1,253</td><td class="c">12</td><td></td></tr>
        <tr><td>3647 Birch ST</td><td>4</td><td>2</td><td class="r">1474</td><td class="r">6111</td><td class="r">1799900</td><td class="c">2115000</td><td class="c">1,435</td><td class="c">17</td><td></td></tr>
        <tr><td>60 Ridgeway CIR</td><td>4</td><td>2</td><td class="r">1456</td><td class="r">6111</td><td class="r">1788000</td><td class="c">2000000</td><td class="c">1374</td><td class="c">11</td><td></td></tr>
        <tr><td>252 Fairmont CT</td><td>3</td><td>2</td><td class="r">1428</td><td class="r">10,624</td><td class="r">1,950,000</td><td class="c">2,100,000</td><td class="c">1471</td><td class="c">20</td><td></td></tr>
      </tbody>
    </table>
  </div>
  <div class="agent-photo" role="img" aria-label="Portrait photo of the agent"></div>
  <div class="agent-line"><span class="agent-sig">Dana Whitfield</span><span>| Relocation Specialist | California Licence #00412987</span></div>
  <div class="contact-band">
    <span><svg width="16" height="12" viewBox="0 0 16 12"><rect x=".5" y=".5" width="15" height="11" fill="none" stroke="#0a5ea8"/><path d="M.5 .5 8 7 15.5 .5" fill="none" stroke="#0a5ea8"/></svg>dwhitfield@hcrealty.com</span>
    <span><svg width="10" height="16" viewBox="0 0 10 16"><rect x="1" y="1" width="8" height="14" rx="1.5" fill="none" stroke="#0a5ea8" stroke-width="1.5"/></svg>650-555-0148</span>
    <span><svg width="12" height="12" viewBox="0 0 12 12"><circle cx="6" cy="6" r="5" fill="none" stroke="#0a5ea8"/><path d="M1 6h10M6 1c-3 3-3 7 0 10M6 1c3 3 3 7 0 10" fill="none" stroke="#0a5ea8"/></svg>www.dwhitfield.com</span>
  </div>
  <p class="disclaimer">*indicates Harbor Crest Realty listing or sale. This information is deemed reliable, but not verified or guaranteed</p>
</section>

<section class="card back">
  <div class="side-panel"></div>
  <h2 class="lead">Traditionally, Feb. through April are the best months to sell</h2>
  <div class="checks">
    <span><svg width="11" height="11" viewBox="0 0 11 11"><rect x=".5" y=".5" width="10" height="10" fill="none" stroke="#0a5ea8"/><path d="M2 5.5 4.5 8 9.5 2" fill="none" stroke="#0a5ea8" stroke-width="1.6"/></svg>Most Offers</span>
    <span><svg width="11" height="11" viewBox="0 0 11 11"><rect x=".5" y=".5" width="10" height="10" fill="none" stroke="#0a5ea8"/><path d="M2 5.5 4.5 8 9.5 2" fill="none" stroke="#0a5ea8" stroke-width="1.6"/></svg>Higest Prices</span>
  </div>
  <p class="reach">Our Listings are advertised locally and <b>in 40 countries!!</b></p>
  <div class="cta"><em>Don't Wait.</em> Call Now for a Private Consultation!</div>
  <div class="body-copy">
    <p>Our market continues to be strong, which reflects both our vibrant and growing local economy and our seemingly chronic shortage of inventory. As long as those conditions continue, our market values will remain high. That is good news to sellers who may want to down-size or move to a different area for a new job, or maybe to be closer to family.</p>
    <p>I am a Harbor Crest Realty certified Relocation Specialist, and, as such, I can connect you with experienced and professional real estate agent anywhere in the country and in most countries around the world. We can co-ordinate your transactions at both ends, making your transition as seamless as possible. If you are planning a move, across the street or across the county, call me now for a confidential consultation.</p>
  </div>
  <div class="back-band"></div>
  <div class="back-photo" role="img" aria-label="Portrait photo of the agent"></div>
  <p class="back-name">Dana Whitfield <small>| License: 00412987</small></p>
  <p class="back-contact">650-555-0148 | dwhitfield@hcrealty.com</p>
  <div class="stamp"></div>
  <div class="back-brand"><span class="mark"></span><span class="brand-name">HARBOR CREST</span></div>
  <p class="back-web"><svg width="11" height="11" viewBox="0 0 12 12"><circle cx="6" cy="6" r="5" fill="none" stroke="#0a5ea8"/><path d="M1 6h10M6 1c-3 3-3 7 0 10M6 1c3 3 3 7 0 10" fill="none" stroke="#0a5ea8"/></svg>www.dwhitfield.com</p>
</section>

</body>
</html>
```